UHT milk packaging Design, (Package Design and Outer Carton Design)

Create a Packaging Design
We would like to you to design a UHT milk packaging. We would need our brand logo on the box (Corvin or Brisko). At present, we do not have a logo design, only the brand name. The Name of the product will be "Full Cream Milk", "Skim Milk", "Lite Milk"

We use Sorvo Kase packaging,
Dimensions of 1L product: 90mm*58mm*195mm
Dimensions of 250ml product: 63mm*40mm*106mm

It should also include:
Barcode placeholder
Area for ingredients
1L and 250ml

Upload files are photoes of other Sorvo Kase packaging

The final design should communicate:
Freshness
Healthy
Modern
Striking

Subsequently, we also have other products packaging that need to be designed, such as muesli, meat, etc

Target Market(s)

family consumption

Font styles to use
Decorative

Requirements
Must have
• Our brand logo (BRISKO);
• Make people feel fresh and healthy
Nice to have
• Bright colors;
• Attractive picture

```html
<!DOCTYPE html>
<html lang="en">
<head>
<meta charset="utf-8">
<title>Brisko UHT Milk – Carton Front Panels</title>
<link rel="stylesheet" href="https://fonts.googleapis.com/css2?family=Playfair+Display:ital,wght@1,400&family=Lato:wght@400&display=swap">
<style>
  :root {
    --bg: #ffffff;
    --ink: #111111;
    --white: #ffffff;
    --green: #86e466;
    --green-soft: #b8f09e;
    --green-stripe: #9be37c;
    --aqua: #7de6d8;
    --aqua-soft: #b3f1e9;
    --aqua-stripe: #8fdde8;
    --orange: #f6a56a;
    --orange-soft: #f9c9a1;
    --orange-stripe: #f3a866;
  }
  * { box-sizing: border-box; margin: 0; padding: 0; }
  html, body { width: 800px; height: 1200px; overflow: hidden; background: var(--bg); }
  .canvas { position: relative; width: 800px; height: 1200px; }

  .carton-front {
    position: absolute; width: 180px; height: 392px; overflow: hidden;
    background: var(--white);
  }
  .carton-front--hero { left: 285px; top: 130px; transform: scale(1.2778); transform-origin: top left; }
  .carton-front--full { left: 54px; top: 772px; }
  .carton-front--lite { left: 306px; top: 772px; }
  .carton-front--skim { left: 558px; top: 772px; }

  .variant-full { --tone: var(--green); --tone-soft: var(--green-soft); --stripe: var(--green-stripe); }
  .variant-lite { --tone: var(--aqua); --tone-soft: var(--aqua-soft); --stripe: var(--aqua-stripe); }
  .variant-skim { --tone: var(--orange); --tone-soft: var(--orange-soft); --stripe: var(--orange-stripe); }

  .stripe-texture {
    position: absolute; inset: 0;
    background: linear-gradient(180deg, var(--stripe) 0%, var(--tone-soft) 30%, var(--tone-soft) 70%, var(--stripe) 100%);
    opacity: 0.55;
  }
  .centre-glow {
    position: absolute; left: -40px; top: 60px; width: 260px; height: 290px;
    background: radial-gradient(ellipse at center, var(--white) 55%, rgba(255,255,255,0) 72%);
  }

  .brand-badge {
    position: absolute; top: 22px; left: 50%; transform: translateX(-50%);
    display: flex; align-items: center; gap: 4px;
    padding: 3px 8px; background: var(--tone-soft);
  }
  .brand-badge__mark { width: 5px; height: 5px; background: var(--white); }
  .brand-badge__name {
    font-family: "Lato", sans-serif; font-size: 9px; letter-spacing: 1px; color: var(--white);
  }

  .milk-blob { position: absolute; left: 0; top: 104px; width: 180px; height: 180px; }

  .product-name {
    position: absolute; left: 0; right: 0; top: 150px; text-align: center;
    font-family: "Playfair Display", serif; font-style: italic; font-weight: 400;
    font-size: 66px; line-height: 1; color: var(--white); letter-spacing: -1px;
  }
  .product-variant {
    position: absolute; left: 112px; top: 248px;
    font-family: "Lato", sans-serif; font-size: 10px; line-height: 1; color: var(--white);
  }

  .volume-tag { position: absolute; left: 80px; bottom: 8px; width: 20px; height: 28px; }
  .volume-tag__dot {
    width: 20px; height: 20px; border-radius: 50%; background: var(--ink); color: var(--white);
    font-family: "Lato", sans-serif; font-size: 10px; line-height: 20px; text-align: center;
  }
  .volume-tag__stem { width: 2px; height: 8px; margin: 0 auto; background: var(--ink); }
</style>
</head>
<body>
<main class="canvas">

  <section class="carton-front carton-front--hero variant-lite">
    <div class="stripe-texture" role="img" aria-label="Horizontal brushed stripe texture in aqua"></div>
    <div class="centre-glow"></div>
    <div class="brand-badge"><span class="brand-badge__mark"></span><span class="brand-badge__name">BRISKO</span></div>
    <svg class="milk-blob" viewBox="0 0 180 180" aria-hidden="true">
      <path fill="var(--tone-soft)" d="M92 2C132-2 166 20 174 52C182 84 176 116 164 140C150 168 120 182 88 178C54 174 22 164 8 134C-4 108 0 70 18 42C36 14 62 6 92 2Z"/>
      <path fill="var(--tone)" d="M95 10C130 4 158 22 166 52C174 82 168 110 156 134C144 158 118 172 90 168C60 164 32 156 18 130C6 106 10 74 26 48C42 22 66 14 95 10Z"/>
    </svg>
    <p class="product-name">milk</p>
    <p class="product-variant">lite</p>
    <div class="volume-tag"><div class="volume-tag__dot">1l</div><div class="volume-tag__stem"></div></div>
  </section>

  <section class="carton-front carton-front--full variant-full">
    <div class="stripe-texture" role="img" aria-label="Horizontal brushed stripe texture in green"></div>
    <div class="centre-glow"></div>
    <div class="brand-badge"><span class="brand-badge__mark"></span><span class="brand-badge__name">BRISKO</span></div>
    <svg class="milk-blob" viewBox="0 0 180 180" aria-hidden="true">
      <path fill="var(--tone-soft)" d="M92 2C132-2 166 20 174 52C182 84 176 116 164 140C150 168 120 182 88 178C54 174 22 164 8 134C-4 108 0 70 18 42C36 14 62 6 92 2Z"/>
      <path fill="var(--tone)" d="M95 10C130 4 158 22 166 52C174 82 168 110 156 134C144 158 118 172 90 168C60 164 32 156 18 130C6 106 10 74 26 48C42 22 66 14 95 10Z"/>
    </svg>
    <p class="product-name">milk</p>
    <p class="product-variant">full<br>cream</p>
    <div class="volume-tag"><div class="volume-tag__dot">1l</div><div class="volume-tag__stem"></div></div>
  </section>

  <section class="carton-front carton-front--lite variant-lite">
    <div class="stripe-texture" role="img" aria-label="Horizontal brushed stripe texture in aqua"></div>
    <div class="centre-glow"></div>
    <div class="brand-badge"><span class="brand-badge__mark"></span><span class="brand-badge__name">BRISKO</span></div>
    <svg class="milk-blob" viewBox="0 0 180 180" aria-hidden="true">
      <path fill="var(--tone-soft)" d="M92 2C132-2 166 20 174 52C182 84 176 116 164 140C150 168 120 182 88 178C54 174 22 164 8 134C-4 108 0 70 18 42C36 14 62 6 92 2Z"/>
      <path fill="var(--tone)" d="M95 10C130 4 158 22 166 52C174 82 168 110 156 134C144 158 118 172 90 168C60 164 32 156 18 130C6 106 10 74 26 48C42 22 66 14 95 10Z"/>
    </svg>
    <p class="product-name">milk</p>
    <p class="product-variant">lite</p>
    <div class="volume-tag"><div class="volume-tag__dot">1l</div><div class="volume-tag__stem"></div></div>
  </section>

  <section class="carton-front carton-front--skim variant-skim">
    <div class="stripe-texture" role="img" aria-label="Horizontal brushed stripe texture in orange"></div>
    <div class="centre-glow"></div>
    <div class="brand-badge"><span class="brand-badge__mark"></span><span class="brand-badge__name">BRISKO</span></div>
    <svg class="milk-blob" viewBox="0 0 180 180" aria-hidden="true">
      <path fill="var(--tone-soft)" d="M92 2C132-2 166 20 174 52C182 84 176 116 164 140C150 168 120 182 88 178C54 174 22 164 8 134C-4 108 0 70 18 42C36 14 62 6 92 2Z"/>
      <path fill="var(--tone)" d="M95 10C130 4 158 22 166 52C174 82 168 110 156 134C144 158 118 172 90 168C60 164 32 156 18 130C6 106 10 74 26 48C42 22 66 14 95 10Z"/>
    </svg>
    <p class="product-name">milk</p>
    <p class="product-variant">skim</p>
    <div class="volume-tag"><div class="volume-tag__dot">1l</div><div class="volume-tag__stem"></div></div>
  </section>

</main>
</body>
</html>
```